Business Cards for a small business advisory (business services)

Professional look. Same as would apply for a lawyer, accountant, or other financial services professional. Please use the logo colors

Target Market(s)

small business owners

Industry/Entity Type

Financial Servics

Contact Information for Business Card

Name: Glenn R. Whitaker, CAIA / Title: Business Advisor / Office #: (555) 284-7193 / Mobile #: (555) 903-6418 / Email: g.whitaker@ambervalebusinessbrokers.example / Web: www.ambervalebusinessbrokers.example

Font styles to use
Sans Serif

```html
<!DOCTYPE html>
<html lang="en">
<head>
<meta charset="utf-8">
<title>Ambervale – Business Cards</title>
<link rel="stylesheet" href="https://fonts.googleapis.com/css2?family=Montserrat:wght@400;500;600;700;800&display=swap">
<style>
  :root {
    --navy: #1e3a6b;
    --green: #8cc63f;
    --white: #ffffff;
    --ink: #1b1b1b;
    --stage: #e6e7ea;
  }
  * { margin: 0; padding: 0; box-sizing: border-box; }
  html, body { width: 1200px; height: 694px; overflow: hidden; }
  body {
    background: var(--stage);
    font-family: "Montserrat", Arial, sans-serif;
    position: relative;
  }
  .card {
    position: absolute;
    top: 192px;
    width: 540px;
    height: 309px;
    overflow: hidden;
    box-shadow: 0 6px 18px rgba(0,0,0,0.15);
  }
  .card--back { left: 40px; background: var(--navy); color: var(--white); }
  .card--front { left: 620px; background: var(--white); color: var(--navy); }

  .brand {
    position: absolute;
    display: flex;
    align-items: center;
    gap: 16px;
  }
  .brand__mark {
    width: 58px; height: 58px; border-radius: 50%;
    flex: none;
  }
  .brand__name {
    font-weight: 700;
    font-size: 58px;
    line-height: 1;
    letter-spacing: 0.5px;
    white-space: nowrap;
  }

  .card--back .brand { left: 50%; top: 50%; transform: translate(-50%, -50%); }
  .card--back .brand__mark { background: var(--white); }

  .card--front .brand { left: 70px; top: 40px; }
  .card--front .brand__mark { background: var(--navy); }

  .person { position: absolute; left: 34px; top: 150px; }
  .person__name { font-weight: 700; font-size: 21px; color: var(--navy); }
  .person__title { font-weight: 400; font-size: 14px; color: var(--ink); margin-top: 2px; }

  .divider {
    position: absolute; left: 34px; right: 26px; top: 207px;
    height: 1px; background: var(--ink);
  }

  .contacts {
    position: absolute; top: 218px;
    list-style: none;
    font-size: 12px; color: var(--ink);
    white-space: nowrap;
  }
  .contacts--phone { left: 34px; }
  .contacts--web { left: 186px; }
  .contacts li { display: flex; align-items: center; gap: 8px; height: 24px; }
  .contacts svg { width: 14px; height: 14px; fill: var(--navy); flex: none; }

  .stripe { position: absolute; left: 0; right: 0; bottom: 0; height: 12px; display: flex; }
  .stripe__navy { flex: 1; background: var(--navy); }
  .stripe__green { width: 112px; background: var(--green); }
</style>
</head>
<body>

  <section class="card card--back" aria-label="Card back">
    <div class="brand">
      <span class="brand__mark"></span>
      <div class="brand__name">Ambervale</div>
    </div>
  </section>

  <section class="card card--front" aria-label="Card front">
    <div class="brand">
      <span class="brand__mark"></span>
      <div class="brand__name">Ambervale</div>
    </div>

    <div class="person">
      <div class="person__name">Glenn R. Whitaker, CAIA</div>
      <div class="person__title">Business Advisor</div>
    </div>

    <div class="divider"></div>

    <ul class="contacts contacts--phone">
      <li>
        <svg viewBox="0 0 24 24" aria-hidden="true"><path d="M3 8c0-2 2-4 9-4s9 2 9 4v2h-5V8H8v2H3zM6 11h12l2 9H4zm6 2a3 3 0 1 0 0 6 3 3 0 0 0 0-6z"/></svg>
        (555) 284-7193
      </li>
      <li>
        <svg viewBox="0 0 24 24" aria-hidden="true"><path d="M7 2h10a2 2 0 0 1 2 2v16a2 2 0 0 1-2 2H7a2 2 0 0 1-2-2V4a2 2 0 0 1 2-2zm0 3v13h10V5zm5 14.2a1 1 0 1 0 0 2 1 1 0 0 0 0-2z"/></svg>
        (555) 903-6418
      </li>
    </ul>

    <ul class="contacts contacts--web">
      <li>
        <svg viewBox="0 0 24 24" aria-hidden="true"><path d="M2 5h20v14H2zm2 2v.5l8 5.5 8-5.5V7zm0 3v7h16v-7l-8 5.5z"/></svg>
        g.whitaker@ambervalebusinessbrokers.example
      </li>
      <li>
        <svg viewBox="0 0 24 24" aria-hidden="true"><path d="M12 2a10 10 0 1 0 0 20 10 10 0 0 0 0-20zm0 2c1.2 0 2.5 2.2 3 5H9c.5-2.8 1.8-5 3-5zM4.3 9h2.7a17 17 0 0 0 0 6H4.3a8 8 0 0 1 0-6zM9 11h6a15 15 0 0 1 0 2H9a15 15 0 0 1 0-2zm8 -2h2.7a8 8 0 0 1 0 6H17a17 17 0 0 0 0-6zM9 15h6c-.5 2.8-1.8 5-3 5s-2.5-2.2-3-5z"/></svg>
        www.ambervalebusinessbrokers.example
      </li>
    </ul>

    <div class="stripe"><span class="stripe__navy"></span><span class="stripe__green"></span></div>
  </section>

</body>
</html>
```